International wholesale business needs a business card

We need a business card.

Company Details:
Company Name and logo
Address, Phone number, Website
Employee Details:
Name, Designation, Mobile Number & Email address

Logo file is attached.

```html
<!DOCTYPE html>
<html lang="en">
<head>
<meta charset="utf-8">
<title>Veluna Trading – Business Card</title>
<link href="https://fonts.googleapis.com/css2?family=Montserrat:wght@400;500;700&display=swap" rel="stylesheet">
<style>
  :root {
    --brand-red: #c8232c;
    --ink-dark: #2a2a2c;
    --card-white: #ffffff;
    --muted-grey: #8a8d91;
    --page-bg: #e6e6e8;
    --on-dark: #f2f2f2;
  }
  * { margin: 0; padding: 0; box-sizing: border-box; }
  html, body { width: 1200px; height: 900px; overflow: hidden; }
  body {
    background: var(--page-bg);
    font-family: "Montserrat", sans-serif;
    position: relative;
  }
  .card {
    position: absolute;
    left: 290px;
    width: 620px;
    height: 354px;
    border-radius: 18px;
    background: var(--card-white);
    overflow: hidden;
    box-shadow: 0 8px 24px rgba(0,0,0,0.12);
  }
  .card--front { top: 66px; }
  .card--back { top: 480px; }

  .brand {
    display: flex;
    align-items: center;
    gap: 16px;
    position: absolute;
  }
  .brand__mark {
    background: var(--muted-grey);
    flex: none;
  }
  .brand__name {
    color: var(--brand-red);
    font-weight: 700;
    letter-spacing: 0.06em;
    white-space: nowrap;
  }
  .card--front .brand { left: 50%; top: 50%; transform: translate(-50%, -50%); }
  .card--front .brand__mark { width: 40px; height: 40px; }
  .card--front .brand__name { font-size: 38px; }

  .card--back .brand { left: 40px; top: 36px; gap: 12px; }
  .card--back .brand__mark { width: 26px; height: 26px; }
  .card--back .brand__name { font-size: 25px; }

  .back-band { position: absolute; inset: 0; }

  .person { position: absolute; left: 40px; top: 112px; }
  .person__name { color: var(--brand-red); font-weight: 700; font-size: 24px; line-height: 30px; }
  .person__role { color: var(--ink-dark); font-size: 14px; font-weight: 500; line-height: 18px; margin-top: 2px; }

  .contacts {
    position: absolute;
    left: 40px;
    top: 240px;
    list-style: none;
    color: var(--on-dark);
    font-size: 13px;
  }
  .contacts li { display: flex; align-items: center; gap: 10px; height: 20px; }
  .contacts svg { width: 13px; height: 13px; fill: var(--brand-red); flex: none; }

  .address {
    position: absolute;
    left: 63px;
    top: 304px;
    color: var(--on-dark);
    font-size: 13px;
    line-height: 18px;
    font-style: normal;
  }
</style>
</head>
<body>
  <section class="card card--front" aria-label="Card front">
    <div class="brand">
      <span class="brand__mark"></span>
      <span class="brand__name">VELUNA TRADING</span>
    </div>
  </section>

  <section class="card card--back" aria-label="Card back">
    <svg class="back-band" width="620" height="354" viewBox="0 0 620 354">
      <polygon points="0,226 620,150 620,354 0,354" fill="var(--ink-dark)"/>
      <line x1="0" y1="226" x2="620" y2="150" stroke="var(--brand-red)" stroke-width="4"/>
    </svg>

    <div class="brand">
      <span class="brand__mark"></span>
      <span class="brand__name">VELUNA TRADING</span>
    </div>

    <div class="person">
      <p class="person__name">Daniel Morel</p>
      <p class="person__role">CEO &amp; Founder</p>
    </div>

    <ul class="contacts">
      <li>
        <svg viewBox="0 0 24 24"><path d="M6.6 10.8a15.1 15.1 0 0 0 6.6 6.6l2.2-2.2a1 1 0 0 1 1-.25 11.4 11.4 0 0 0 3.6.57 1 1 0 0 1 1 1V20a1 1 0 0 1-1 1A17 17 0 0 1 3 4a1 1 0 0 1 1-1h3.5a1 1 0 0 1 1 1c0 1.25.2 2.45.57 3.6a1 1 0 0 1-.25 1z"/></svg>
        955 41 27 80
      </li>
      <li>
        <svg viewBox="0 0 24 24"><path d="M2 5h20v14H2zM4 7v.5l8 5 8-5V7l-8 5z"/></svg>
        info@velunatrading.com
      </li>
      <li>
        <svg viewBox="0 0 24 24"><path d="M12 2a10 10 0 1 0 0 20 10 10 0 0 0 0-20zm0 2c1.2 1.5 2 3.6 2.2 7H9.8c.2-3.4 1-5.5 2.2-7zM9.8 13h4.4c-.2 3.4-1 5.5-2.2 7-1.2-1.5-2-3.6-2.2-7z"/></svg>
        www.velunatrading.com
      </li>
    </ul>

    <address class="address">
      Pol. Ind. Lumbre, C/3 nº 8 2<br>
      2200 Villanueva del Campo
    </address>
  </section>
</body>
</html>
```